Modern Innovative Business Card Design

We require a nice, modern, clean business card design, ready for upload to Cardomora. Our company develops online banking software solutions for small financial insitutions. The design should be clean, professional, but yet not "corporate boring". See www.fyrolt.com for an idea of business image and profile. The design should communicate innovation, be modern and fresh, yet look professional and established.

Target Market(s)

Finance industry, bankers, entrepreneurs

Industry/Entity Type

Financial

Contact Information for Business Card

Tobias Wendlerup
CEO

FYROLT BV
Lindenwerf 38
1027 HX Amsterdam
The Netherlands

Phone: +31 20 517 8036
Direct: +31 20 604 1758
Skype: tobias.fyrolt
ceo@fyrolt.com
www.fyrolt.com

Font styles to use
Sans Serif

Requirements
Must have
• Should look clean, modern and professional. File should be ready for upload to cardomora.
Should not have
• Boring standard corporate layout

```html
<!DOCTYPE html>
<html lang="en">
<head>
<meta charset="utf-8">
<title>FYROLT Business Card</title>
<link href="https://fonts.googleapis.com/css2?family=Open+Sans:wght@300;400;600&display=swap" rel="stylesheet">
<style>
  :root {
    --card-light: #505050;
    --card-dark: #232323;
    --band: #2a2a2a;
    --lime: #8dc63f;
    --ink: #111111;
    --paper: #ffffff;
    --white: #ffffff;
  }
  * { margin: 0; padding: 0; box-sizing: border-box; }
  html, body {
    width: 930px; height: 1200px; overflow: hidden;
    background: var(--paper);
    font-family: "Open Sans", Arial, sans-serif;
  }
  .sheet { position: relative; width: 930px; height: 1200px; }
  .card {
    position: absolute; left: 0; width: 930px; height: 533px; overflow: hidden;
    background: radial-gradient(ellipse 75% 70% at 55% 40%, var(--card-light) 0%, #3a3a3a 45%, var(--card-dark) 100%);
  }
  .card--front { top: 0; }
  .card--back { top: 668px; height: 532px; }
  .card__shapes { position: absolute; inset: 0; }
  .panel { fill: var(--lime); filter: drop-shadow(6px 8px 6px rgba(0,0,0,.55)); }
  .diagonal-band { fill: var(--band); filter: drop-shadow(8px 6px 8px rgba(0,0,0,.6)); }
  .wordmark {
    font-family: "Open Sans", Arial, sans-serif;
    font-weight: 600; font-size: 74px; letter-spacing: 2px; fill: var(--white);
  }
  .icon { fill: var(--lime); }
  .text { position: absolute; white-space: nowrap; line-height: 1; }
  .holder-name { left: 308px; top: 140px; font-size: 48px; font-weight: 400; color: var(--ink); }
  .holder-role { left: 308px; top: 195px; font-size: 38px; font-weight: 300; color: var(--ink); }
  .contact-list, .address {
    position: absolute; right: 115px; text-align: right; list-style: none;
    font-size: 30px; font-weight: 400; color: var(--ink); text-transform: uppercase;
  }
  .contact-list { top: 262px; }
  .contact-list li { height: 43px; line-height: 30px; }
  .address { right: 118px; top: 150px; font-size: 31px; }
  .address span { display: block; height: 41px; line-height: 31px; }
  .website { right: 118px; top: 343px; font-size: 31px; color: var(--white); text-transform: uppercase; }
</style>
</head>
<body>
<main class="sheet">
  <section class="card card--front" aria-label="Front of business card">
    <svg class="card__shapes" width="930" height="533" viewBox="0 0 930 533">
      <polygon class="panel" points="308,133 830,133 830,394 148,394"/>
      <polygon class="diagonal-band" points="292,80 334,80 115,438 110,405"/>
      <text class="wordmark" transform="translate(58,392) rotate(-51.5)">FYROLT</text>
      <g class="icon" transform="translate(842,270)">
        <path d="M3 2 L8 1 L11 7 L8 9 Q10 14 15 16 L17 13 L23 16 L22 21 Q14 23 7 16 Q1 9 3 2 Z"/>
      </g>
      <circle class="icon" cx="852" cy="320" r="12"/>
      <g class="icon" transform="translate(840,354)">
        <rect x="0" y="0" width="24" height="17" rx="2"/>
        <path d="M1 1 L12 10 L23 1" fill="none" stroke="#3a3a3a" stroke-width="2"/>
      </g>
    </svg>
    <h1 class="text holder-name">TOBIAS Wendlerup</h1>
    <p class="text holder-role">CEO</p>
    <ul class="contact-list">
      <li>+31 20 604 1758</li>
      <li>tobias.fyrolt</li>
      <li>ceo@fyrolt.com</li>
    </ul>
  </section>

  <section class="card card--back" aria-label="Back of business card">
    <svg class="card__shapes" width="930" height="532" viewBox="0 0 930 532">
      <polygon class="panel" points="314,133 828,133 828,282 215,282"/>
      <polygon class="panel" points="190,319 823,319 823,388 140,388"/>
      <polygon class="diagonal-band" points="296,80 338,80 119,438 114,405"/>
      <text class="wordmark" transform="translate(62,392) rotate(-51.5)">FYROLT</text>
    </svg>
    <address class="address" style="font-style:normal">
      <span>FYROLT BV Lindenwerf</span>
      <span>38 1027 HX Amsterdam</span>
      <span>The Netherlands</span>
    </address>
    <p class="text website">www.fyrolt.com</p>
  </section>
</main>
</body>
</html>
```